Popup Nightclub Grand Opening Flyer

We need to design a flyer for the grand opening of an upscale, exclusive nightclub called "Lanternfall". The design needs to be chic and exclusive. The background should be black and the text should primarily be white. We like minimalist designs.

Here is the text for the flyer
-
Velvetrope Atlanta Presents

Lanternfall (LOGO)

A Popup Nightclub Experience
For one night Only

Friday, October 18, 2013
Party begins at 9PM

INVITE ONLY

See invitation for location details
(Velvetrope Atlanta logo)

-
Examples we like

http://cdn2-b.brivelpost.com/sites/default/files/styles/image_content_width/hash/3d/fa/1472093815_4471_flyer.jpg?itok=R8kqWm2z

http://api.plovra.com/files/7Kqq-Tr82XXB3pQzJvmtR5HL2W719E4nbRtC6KLd4HsfM8Y2qTDK-VmjwDoNqLX4QBzTHD9nakRbVx3m-Pfq8htc3MDTWr5p4/2zelSaturdays.jpg

http://quenmar.com/wp-content/uploads/yootheme/widgetkit/gallery/2zel/2zel-gen_vroom4-01.jpg

Hi All, one thing that we are seeing that we don't like is on over emphasis on the phrase "a popup nightclub experience" please don't make this the largest thing on the flyer

Target Market(s)

Target market is 25-35 year olds who are affluent (rich) and like luxury brands

Requirements
Must have
• Dark Background
Nice to have
• Velvetrope Logo on the bottom
Modern text that isn't curvy
Should not have
• Curved text

```html
<!DOCTYPE html>
<html lang="en">
<head>
<meta charset="utf-8">
<title>Lanternfall Nightclub – Velvetrope Atlanta</title>
<link rel="stylesheet" href="https://fonts.googleapis.com/css2?family=Righteous&family=Montserrat:wght@400&display=swap">
<style>
  :root {
    --bg: #000000;
    --silver: #d9d9d9;
    --grey: #9a9a9a;
    --ice: #a9dbe6;
    --white: #ffffff;
    --mark: #c4c4c4;
  }
  html, body {
    margin: 0;
    padding: 0;
    width: 928px;
    height: 1200px;
    overflow: hidden;
    background: var(--bg);
  }
  .flyer {
    position: relative;
    width: 928px;
    height: 1200px;
    background: var(--bg);
  }
  .flyer p, .flyer h1 { margin: 0; }
  .line {
    position: absolute;
    left: 0;
    width: 928px;
    text-align: center;
    font-family: "Righteous", sans-serif;
    font-weight: 400;
    text-transform: uppercase;
    color: transparent;
    -webkit-text-stroke: 1.6px var(--silver);
    white-space: nowrap;
    line-height: 1;
  }
  .presenter { top: 30px; font-size: 51px; letter-spacing: 2px; }
  .access {
    top: 154px; font-size: 36px; word-spacing: 120px;
    -webkit-text-stroke-color: var(--grey);
  }
  .venue-mark {
    position: absolute;
    left: 314px;
    top: 204px;
    width: 300px;
    height: 300px;
    border-radius: 50%;
    background: var(--mark);
  }
  .venue-name {
    position: absolute;
    left: 0;
    width: 928px;
    top: 516px;
    text-align: center;
    font-family: "Montserrat", sans-serif;
    font-weight: 400;
    font-size: 78px;
    letter-spacing: 10px;
    color: var(--white);
    line-height: 1;
    white-space: nowrap;
  }
  .venue-type {
    position: absolute;
    left: 0;
    width: 928px;
    top: 660px;
    text-align: center;
    font-family: "Montserrat", sans-serif;
    font-weight: 400;
    font-size: 44px;
    letter-spacing: 5px;
    color: var(--white);
    line-height: 1;
  }
  .date { top: 746px; font-size: 68px; letter-spacing: 1px; -webkit-text-stroke-color: var(--ice); }
  .start-time { top: 877px; font-size: 48px; letter-spacing: 2px; -webkit-text-stroke-color: var(--ice); }
  .concept { top: 963px; font-size: 45px; letter-spacing: 2px; }
  .run { top: 1025px; font-size: 44px; letter-spacing: 2px; }
  .location-note {
    top: 1151px; left: 30px; width: auto; text-align: left;
    font-size: 36px; letter-spacing: 1px;
  }
  .host-name {
    position: absolute;
    left: 770px;
    top: 1160px;
    font-family: "Righteous", sans-serif;
    font-size: 21px;
    color: var(--white);
    line-height: 1;
    letter-spacing: 1px;
    white-space: nowrap;
  }
</style>
</head>
<body>
  <main class="flyer">
    <p class="line presenter">Velvetrope Atlanta Presents</p>
    <p class="line access">Invite Only</p>

    <div class="venue-mark" aria-hidden="true"></div>
    <h1 class="venue-name">LANTERNFALL</h1>
    <p class="venue-type">NIGHTCLUB</p>

    <p class="line date">Friday, October 18, 2013</p>
    <p class="line start-time">Party Begins at 9PM</p>
    <p class="line concept">A Popup Nightclub Experience</p>
    <p class="line run">For One Night Only</p>

    <p class="line location-note">See Invitation for Location Details</p>
    <p class="host-name">VELVETROPE</p>
  </main>
</body>
</html>
```